PIPE RELINING COMPANY NEEDS A NEW INFORMATIVE FLYER CREATED

We are a company that sells a service to residential homeowners (using a particular state of the art international product) and we need to refresh our A4 tri- fold flyer (z fold 6 pages). The layout needs to include pictures, heading and text boxes, but be simple and clean cut at the same time.

The front of the flyer must have the attached picture of the pipe under the house, logo and website.

This flyer is going to be given to clients and to leave with them when we quote for work.

Our colour scheme is black, white, red. A highlight colour if needed (in small amounts) could be 100% cyan and also a bright orange.

I have attached the copy of the text and this can be spread out throughout the brochure.

We are a professional and industry leading company so it needs to be professional, clean cut but with a modern edge.

Target Market(s)

HOMEOWNERS

Industry/Entity Type

It Company

Font styles to use
Sans Serif

Colors
ec1f27
ffffff
000000
f37122

Requirements
Must have
• PROFESSINAL, MODERN
• USE OF BLACK, RED AND WHITE - REFER LOGO
Should not have
• BE CLUTTERED

```html
<!DOCTYPE html>
<html lang="en">
<head>
<meta charset="utf-8">
<title>Pipe Relining Tri-fold Brochure</title>
<link href="https://fonts.googleapis.com/css2?family=Open+Sans:ital,wght@0,400;0,600;0,700;0,800;1,700&display=swap" rel="stylesheet">
<style>
  :root{
    --red:#ec1f27;
    --red-dark:#b8141b;
    --black:#000000;
    --charcoal:#1b1b1b;
    --graphite:#3a3a3a;
    --white:#ffffff;
    --paper:#f1f1f1;
    --ink:#222222;
    --stage:#d9d9d9;
    --font:'Open Sans', Arial, sans-serif;
  }
  *{box-sizing:border-box;margin:0;padding:0}
  html,body{width:1200px;height:800px;overflow:hidden;background:var(--stage);font-family:var(--font)}
  .brochure{position:absolute;left:20px;top:20px;width:1160px;height:760px;display:grid;grid-template-columns:repeat(3,1fr);box-shadow:0 6px 24px rgba(0,0,0,.25)}
  .panel{position:relative;overflow:hidden;padding:0 30px}
  .panel--dark{background:radial-gradient(ellipse at 50% 45%,var(--graphite) 0%,var(--charcoal) 55%,var(--black) 100%);color:var(--white)}
  .panel--light{background:linear-gradient(180deg,var(--white) 0%,var(--paper) 100%);color:var(--ink)}

  p{font-size:11.4px;line-height:1.42;margin-bottom:10px}
  .statement{color:var(--red);font-weight:700;font-size:15.5px;line-height:1.3;margin:14px 0 16px}
  .pill{display:inline-block;background:var(--red);color:var(--white);font-weight:700;font-size:12.5px;padding:7px 24px 7px 30px;margin:4px 0 14px -30px;border-radius:0 20px 20px 0}

  /* left panel */
  .hero-photo{position:absolute;left:0;top:0;width:100%;height:200px;background:linear-gradient(135deg,#5a4a3a 0%,#8a7660 35%,#3f6a38 60%,#2a2a24 100%)}
  .hero-swoosh{position:absolute;left:0;top:150px;width:100%;height:90px}
  .panel--left .content{position:relative;padding-top:240px}

  /* middle panel */
  .head-band{position:absolute;left:0;top:0;width:100%;height:240px}
  .panel-title{position:relative;color:var(--white);font-weight:700;font-size:20px;line-height:1.2;padding-top:30px}
  .compare{position:relative;display:flex;gap:40px;margin:26px 0 0 40px;height:110px}
  .compare__shot{width:96px;height:96px;border-radius:50%;border:4px solid var(--white);box-shadow:0 0 0 2px var(--black);position:relative;display:flex;justify-content:center;padding-top:12px}
  .compare__shot--before{background:radial-gradient(circle at 50% 55%,#2a1a14 0%,#7b4a3a 30%,#b58270 70%)}
  .compare__shot--after{background:radial-gradient(circle at 50% 55%,#1a2a12 0%,#2d6b2a 35%,#5ab04a 75%);margin-top:-20px}
  .compare__label{color:var(--white);font-size:10px;font-weight:700;letter-spacing:.5px}
  .panel--middle .content{position:relative;padding-top:24px}

  .ticks{list-style:none}
  .ticks li{position:relative;padding-left:22px;font-size:11.2px;line-height:1.38;margin-bottom:7px}
  .ticks li::before{content:"";position:absolute;left:0;top:2px;width:12px;height:12px;border:1.5px solid var(--red);border-radius:50%}
  .ticks li::after{content:"";position:absolute;left:4px;top:4.5px;width:4px;height:6px;border:solid var(--red);border-width:0 2px 2px 0;transform:rotate(40deg)}

  /* right panel */
  .panel--right .content{padding-top:40px}
  .section-label{font-size:11.5px;font-weight:700;letter-spacing:.3px;margin-bottom:14px}
  .benefits{list-style:none}
  .benefits li{font-size:11.2px;line-height:1.42;margin-bottom:6px}
  .benefits b{color:var(--red);font-weight:700}
  .right-row{display:flex;align-items:center;gap:10px;margin:16px 0 18px}
  .right-row .statement{margin:0;flex:1;font-size:15px}
  .brand{display:flex;flex-direction:column;align-items:center;gap:6px;width:96px}
  .brand__dot{width:46px;height:46px;border-radius:50%;background:var(--red)}
  .brand__name{font-weight:700;font-size:13px;color:var(--white)}
  .panel--right .ticks li{font-size:11.6px;margin-bottom:8px}
</style>
</head>
<body>
<main class="brochure">

  <section class="panel panel--dark panel--left">
    <div class="hero-photo" role="img" aria-label="Photo of tree roots around an exposed drain pipe under a house"></div>
    <svg class="hero-swoosh" viewBox="0 0 387 90" preserveAspectRatio="none" aria-hidden="true">
      <path d="M0 40 Q190 95 387 20 L387 50 Q190 110 0 60 Z" fill="var(--red)"/>
      <path d="M0 60 Q190 110 387 50 L387 90 L0 90 Z" fill="#111"/>
    </svg>
    <div class="content">
      <p>Sewers back up in properties due to ageing lines, misaligned joints, root infestation, calcification and ground movement, costing property owners thousands of dollars in damage to their homes and landscaping.</p>
      <p>Pipe relining eliminates the need for costly excavations to expose and replace this damaged pipework. Pipe Relining is the process of installing a new pipe within the old.</p>
      <p class="statement">Why replace all of your drainage pipes when you can permanently repair the broken sections without destroying your environment.</p>
      <h2 class="pill">What Does Pipe Relining Mean?</h2>
      <p>Pipe relining is the method of repairing existing pipework from within the pipe itself. This is done by using the latest technology to insert a strong internal liner inside the existing pipe.</p>
      <p>During this process the resin impregnated side of the liner is pressed against the wall of the original host pipe at a specified pressure. This pressure ensures 100% resin contact and extrudes resin into all pipe joints, cracks and breaks ensuring no future tree root ingress or pipe movement is possible.</p>
      <p>Pipe relining can be undertaken in either short sectional repair, or long lengths utilising the inversion relining method.</p>
    </div>
  </section>

  <section class="panel panel--light panel--middle">
    <svg class="head-band" viewBox="0 0 387 240" preserveAspectRatio="none" aria-hidden="true">
      <path d="M0 0 L387 0 L387 20 Q300 30 280 110 Q260 175 0 190 Z" fill="var(--red)"/>
      <path d="M387 20 Q330 40 320 110 Q360 60 387 70 Z" fill="var(--red-dark)" opacity=".5"/>
    </svg>
    <h1 class="panel-title">Which Problems Can<br>Pipe Relining Repair?</h1>
    <div class="compare">
      <div class="compare__shot compare__shot--before" role="img" aria-label="Inside view of a cracked, root infested pipe before relining"><span class="compare__label">BEFORE</span></div>
      <div class="compare__shot compare__shot--after" role="img" aria-label="Inside view of the same pipe after relining with a smooth liner"><span class="compare__label">AFTER</span></div>
    </div>
    <div class="content">
      <p>Pipe relining can repair broken, cracked or root infested pipes, pipes with missing sections and pipes that continually block.</p>
      <p>No matter if the pipes are vertical, horizontal or concealed, they all can be repaired. Sections of broken pipes can be relined, without having to replace the entire pipeline.</p>
      <h2 class="pill">Patch Repair Process</h2>
      <ul class="ticks">
        <li>Clean the line with a high pressure water jetter, and carry out a camera inspection to determine the exact location and cause of the problems.</li>
        <li>Prepare the liner. Cut the liner to the correct length, mix the appropriate amount of resin and impregnate the resin into the liner.</li>
        <li>Invert the liner into the pipe, inflate and then cure.</li>
        <li>A seamless, flexible liner is cut to length and filled with environmentally safe epoxy resin. The liner is then inverted into the existing host pipe and inflated using compressed air. Once the liner is fully cured with hot water, it is ready for use.</li>
        <li>The result is a completely new pipe inside the old. This pipe within a pipe is 100% water tight, stronger than PVC pipe, and has an increased flow rate compared to most existing pipes. Relined pipes have a life expectancy of 50 years and our installation work has a 25 year guarantee.</li>
      </ul>
    </div>
  </section>

  <section class="panel panel--dark panel--right">
    <div class="content">
      <h2 class="section-label">BENEFITS OF PIPE RELINING</h2>
      <ul class="benefits">
        <li><b>QUICK INSTALLATION</b> – Most relining jobs can be completed in the same day without the mess and disruption of excavation.</li>
        <li><b>LONG LIFE PRODUCT</b> – Pipe Relining is a long term solution with a 50 year life expectancy.</li>
        <li><b>MINIMAL DISRUPTION</b> – Save your landscapes, trees and driveways.</li>
        <li><b>ECONOMICAL</b> – Save on the cost, time and hassle of restoring your property and landscaping.</li>
        <li><b>INSTALLATION GUARANTEE</b> – Clearbore offer a 25 year warranty, twice that of standard excavations. This also includes an annual warranty camera inspection.</li>
      </ul>
      <div class="right-row">
        <p class="statement">Provides a solution to the whole problem, not just temporary relief from the symptoms.</p>
        <div class="brand">
          <span class="brand__dot"></span>
          <span class="brand__name">Clearbore</span>
        </div>
      </div>
      <h2 class="pill">What Does Pipe Relining Mean?</h2>
      <ul class="ticks">
        <li>Permanent jointless liner</li>
        <li>50 years life expectancy</li>
        <li>Up front price</li>
        <li>Environmentally sound</li>
        <li>Eliminates structural disturbances</li>
        <li>Impervious to future root penetration</li>
        <li>Provides increased flow characteristics</li>
        <li>Suitable for industrial, residential and commercial applications</li>
      </ul>
    </div>
  </section>

</main>
</body>
</html>
```